Stylist/Barber Standup Sign for Hair Regrowth Company

We want to design an attractive and eye-catching sign for hair stylists and barbers to sit on their workstations to attract the attention of their clients regarding hair loss and encourage them to speak to their stylist about it of they are would like to seek treatment.
50% of men and 25% of women suffer from hair loss but most are in denial that it is happening or too embarrassed to talk about it.

Copy for the flyer is as follows:

[Section 1:]
This flyer has been placed here/designed to spark conversation about hair loss

[Section 2:]
The truth is...
73% of people believe their hair is thinning
They are right

[Section 3:]
If you've got questions, your stylist or barber has answers.

Additional Background Information:

Primary target audience is men between the ages of 25-45, secondary target audience is men 46-60

Current Consumer Perception? (in the first person) “I’ve been thinking about my hair. I think it’s getting thinner and I’m scared, worried and don’t know what to do. But I don’t know if there is anything that really works. I’ve tried other things and nothing‘s worked.”

Tonality of materials? Very guy friendly, matter of fact, authoritative, its what you might hear from your best friend. Confident. Encouraging, but with a sense of urgency.

Please use our brand colors, but do not include our logo or brand name.
Colors are as follows:
Green: #4ca26f
Light Grey: #999999
Dark Grey: #262626

I have attached print templates in both PDF and Jpeg, please use those to provide final ready to print documents if you are selected.

Target Market(s)

Industry/Entity Type

Health And Wellness

Font styles to use
Sans Serif

Colors
00a990
ffffff
333333
cbcbcb

Requirements
Must have
• We want to get across the following messaging. Ideally you will submit a design using our copy and if you think you can do better, please feel free to submit another design with your own copy/messaging. If you can do it better we would love to select you :-)
• Our copy?
• This flyer has been placed here/designed to spark conversation about hair loss
• The truth is...
• 73% of people believe their hair is thinning
• They are right
• If you've got questions, your stylist or barber has answers
• Also please use our brand colors:
• Green: #4ca26f
• Light Grey: #999999
• Dark Grey: #262626
Should not have
• dont add any logos, images or ornate design. this needs to be simple, easy to ready and eye catching.
• do not use the color red in any capacity.

```html
<!DOCTYPE html>
<html lang="en">
<head>
<meta charset="utf-8">
<title>Hair Loss Conversation Flyer</title>
<link href="https://fonts.googleapis.com/css2?family=Gafata&family=Yanone+Kaffeesatz:wght@300;400&family=Ovo&display=swap" rel="stylesheet">
<style>
  :root {
    --bg-dark: #333333;
    --teal: #00a990;
    --teal-panel: #17a690;
    --ink-dark: #2a2a2a;
    --ink-deep-teal: #1d4f46;
    --white: #ffffff;
    --light-grey: #e6e6e6;
  }
  html, body {
    margin: 0;
    padding: 0;
    overflow: hidden;
    background: var(--bg-dark);
  }
  .flyer {
    position: relative;
    width: 806px;
    height: 1200px;
    background: var(--bg-dark);
    overflow: hidden;
  }
  .intro {
    position: absolute;
    top: 56px;
    left: 0;
    width: 100%;
    text-align: center;
    font-family: "Gafata", sans-serif;
    color: var(--light-grey);
    font-size: 40px;
    line-height: 56px;
  }
  .intro .accent {
    color: var(--teal);
  }
  .intro .lead {
    font-size: 46px;
  }
  .truth-panel {
    position: absolute;
    left: 0;
    top: 0;
    width: 806px;
    height: 1200px;
  }
  .truth-text {
    position: absolute;
    left: 46px;
    top: 470px;
    width: 718px;
    font-family: "Yanone Kaffeesatz", sans-serif;
    font-weight: 300;
    color: var(--ink-dark);
  }
  .truth-heading {
    margin: 0;
    font-size: 62px;
    line-height: 68px;
    font-weight: 400;
  }
  .truth-stat {
    margin: 4px 0 0;
    font-size: 47px;
    line-height: 58px;
    color: var(--ink-deep-teal);
    white-space: nowrap;
  }
  .truth-stat .figure {
    color: var(--white);
  }
  .truth-verdict {
    margin: 4px 0 0;
    text-align: right;
    font-size: 47px;
    line-height: 58px;
    color: var(--ink-dark);
  }
  .closing {
    position: absolute;
    top: 1010px;
    left: 0;
    width: 100%;
    text-align: center;
    font-family: "Ovo", serif;
    color: var(--light-grey);
    font-size: 40px;
    line-height: 66px;
  }
</style>
</head>
<body>
<main class="flyer">
  <section class="intro">
    <div class="lead accent">This flyer</div>
    <div>has been placed here/designed to</div>
    <div><span class="accent">spark</span> conversation about hair loss</div>
  </section>

  <svg class="truth-panel" viewBox="0 0 806 1200" aria-hidden="true">
    <path fill="var(--teal-panel)" d="M40,410 L60,395 75,412 110,405 130,385 150,410 200,402 240,408 260,390 275,409 330,404 390,410 420,396 440,409 500,403 560,408 590,392 605,410 660,404 700,409 720,388 735,408 770,403 785,385 775,420 778,450 795,470 776,490 780,560 800,585 778,600 776,680 790,700 774,720 778,770 795,790 760,775 740,795 720,774 650,778 600,772 580,792 560,776 480,774 420,778 400,796 385,776 300,772 240,778 220,798 205,776 130,774 90,779 70,796 55,775 35,790 42,760 40,700 20,680 42,660 38,560 15,540 40,520 42,450 22,430 40,420 Z"/>
  </svg>

  <section class="truth-text">
    <h2 class="truth-heading">The truth is...</h2>
    <p class="truth-stat"><span class="figure">73%</span> of people believe their hair is thinning</p>
    <p class="truth-verdict">They are right</p>
  </section>

  <section class="closing">
    <div>If you've got questions,</div>
    <div>your stylist or barber has answers.</div>
  </section>
</main>
</body>
</html>
```